Telmoro Business Card

I already have the conplay logo. I need to develop a professional business card layout

Target Market(s)

Business

Industry/Entity Type

Business

Contact Information for Business Card

Company Name: Telmoro Limited

Font styles to use
Sans Serif

Colors

Designer to choose colors to be used in the design.

Requirements
Must have
• Use current logo
• Need two card size options:
• Small Card: 70mm x 28mm (Landscape)
• Square Card: 65mm x 65mm
Nice to have
• I will need 8-10 files for each name, number and email address (details to follow)

```html
<!DOCTYPE html>
<html lang="en">
<head>
<meta charset="utf-8">
<title>Telmoro Limited – Business Cards</title>
<link rel="stylesheet" href="https://fonts.googleapis.com/css2?family=Questrial&display=swap">
<style>
  :root {
    --navy: #2b2a7a;
    --green: #8dc63f;
    --band-green: #a5cd63;
    --yellow: #e8d72a;
    --orange: #dd6330;
    --slate: #465280;
    --phone-red: #e0262b;
    --mail-orange: #f5a623;
    --paper: #ffffff;
    --canvas: #ffffff;
  }
  * { box-sizing: border-box; margin: 0; padding: 0; }
  html, body {
    width: 1200px; height: 1200px; overflow: hidden;
    background: var(--canvas);
    font-family: "Questrial", "Century Gothic", sans-serif;
    color: var(--navy);
  }
  .stage { position: relative; width: 1200px; height: 1200px; }

  .card {
    position: absolute; background: var(--paper); overflow: hidden;
    box-shadow: 0 0 6px rgba(0,0,0,.35);
  }
  .card--square { left: 36px; top: 50px; width: 722px; height: 724px; border-radius: 48px; }
  .card--slim { left: 794px; top: 146px; width: 366px; height: 914px; }

  .card__band {
    position: absolute; left: 0; bottom: 0; width: 100%;
    background: linear-gradient(100deg,
      var(--yellow) 0%, var(--band-green) 30%, var(--orange) 48%,
      var(--band-green) 68%, var(--slate) 100%);
    opacity: .9;
  }
  .card--square .card__band { height: 150px; }
  .card--slim .card__band { height: 78px; }

  .brand { position: absolute; text-align: center; white-space: nowrap; }
  .brand__name { display: block; color: var(--navy); line-height: 1; }
  .brand__legal { display: block; color: var(--navy); letter-spacing: .09em; line-height: 1; }

  .card--square .brand { left: 290px; top: 46px; width: 430px; }
  .card--square .brand__name { font-size: 86px; letter-spacing: .02em; }
  .card--square .brand__legal { font-size: 37px; margin-top: 6px; }

  .card--slim .brand { left: 0; top: 70px; width: 366px; }
  .card--slim .brand__name { font-size: 56px; letter-spacing: .02em; }
  .card--slim .brand__legal { font-size: 22px; margin-top: 8px; }

  .person { position: absolute; white-space: nowrap; }
  .person__name { display: block; letter-spacing: .08em; line-height: 1; }
  .person__role { display: block; color: var(--green); letter-spacing: .09em; line-height: 1; }

  .card--square .person { left: 17px; top: 266px; }
  .card--square .person__name { font-size: 36px; }
  .card--square .person__role { font-size: 25px; margin-top: 2px; }

  .card--slim .person { left: 29px; top: 258px; }
  .card--slim .person__name { font-size: 29px; }
  .card--slim .person__role { font-size: 20px; margin-top: 1px; }

  .contact { list-style: none; white-space: nowrap; }
  .contact__item { display: flex; align-items: center; }
  .contact__icon { flex: none; }

  .card--square .contact { position: absolute; left: 17px; top: 364px; }
  .card--square .contact__item { font-size: 24px; letter-spacing: .04em; height: 34px; }
  .card--square .contact__item + .contact__item { margin-top: 1px; }
  .card--square .contact__icon { width: 28px; height: 28px; margin-right: 8px; }

  .card--slim .contact { margin-top: 30px; }
  .card--slim .contact__item { font-size: 19.5px; letter-spacing: .04em; height: 28px; }
  .card--slim .contact__icon { width: 22px; height: 22px; margin-right: 7px; }
</style>
</head>
<body>
<main class="stage">

  <section class="card card--square" aria-label="Square business card">
    <div class="brand">
      <span class="brand__name">TELMORO</span>
      <span class="brand__legal">TELMORO LIMITED</span>
    </div>

    <div class="person">
      <span class="person__name">ALEX REED</span>
      <span class="person__role">Manager</span>
    </div>

    <ul class="contact">
      <li class="contact__item">
        <svg class="contact__icon" viewBox="0 0 24 24"><path fill="var(--green)" d="M12 2 1 12h3v9h6v-6h4v6h6v-9h3z"/></svg>
        123 street address country
      </li>
      <li class="contact__item">
        <svg class="contact__icon" viewBox="0 0 24 24"><path fill="var(--phone-red)" d="M7 2 4 3c-2 5 2 14 9 18l3-1 2-4-4-2-2 2c-2-1-4-5-4-7l2-1-1-5z"/></svg>
        000 123 4567 8900
      </li>
      <li class="contact__item">
        <svg class="contact__icon" viewBox="0 0 24 24"><rect x="1" y="6" width="22" height="14" fill="var(--mail-orange)"/><path d="M1 6l11 8 11-8M1 20l8-7M23 20l-8-7" fill="none" stroke="#fff" stroke-width="1.3"/></svg>
        company’s mail@mail.com
      </li>
    </ul>

    <div class="card__band" role="img" aria-label="Decorative multicolour geometric band in green, yellow, orange and slate blue"></div>
  </section>

  <section class="card card--slim" aria-label="Slim business card">
    <div class="brand">
      <span class="brand__name">TELMORO</span>
      <span class="brand__legal">TELMORO LIMITED</span>
    </div>

    <div class="person">
      <span class="person__name">ALEX REED</span>
      <span class="person__role">Manager</span>
      <ul class="contact">
        <li class="contact__item">
          <svg class="contact__icon" viewBox="0 0 24 24"><path fill="var(--green)" d="M12 2 1 12h3v9h6v-6h4v6h6v-9h3z"/></svg>
          123 street address country
        </li>
        <li class="contact__item">
          <svg class="contact__icon" viewBox="0 0 24 24"><path fill="var(--phone-red)" d="M7 2 4 3c-2 5 2 14 9 18l3-1 2-4-4-2-2 2c-2-1-4-5-4-7l2-1-1-5z"/></svg>
          000 123 4567 8900
        </li>
        <li class="contact__item">
          <svg class="contact__icon" viewBox="0 0 24 24"><rect x="1" y="6" width="22" height="14" fill="var(--mail-orange)"/><path d="M1 6l11 8 11-8M1 20l8-7M23 20l-8-7" fill="none" stroke="#fff" stroke-width="1.3"/></svg>
          company’s mail@mail.com
        </li>
      </ul>
    </div>

    <div class="card__band" role="img" aria-label="Decorative multicolour geometric band in green, yellow, orange and slate blue"></div>
  </section>

</main>
</body>
</html>
```